Wine Label Design for a white wine made in the region of San Gimignano, Italy

This is a white wine (crisp and fresh) that is made in the region of San Gimignano, Italy, which is a beautiful hill town in Tuscany famous for it's towers. We would like a classy, elegant front wine label that can also be somewhat fun and whimsical if you prefer. Showcasing or depicting or alluding to the town and the towers of San Gimignano is a plus. The label should state the brand name which is "Cortivane", the varietal, which is Vernaccia di San Gimignano, and the vintage which is 2015. We might change the size of the label slightly but for design purposes please use 5 inches wide x 5 1/2 inches tall. I've uploaded a photo of a successful label design for parameters, but you should not feel limited to this either. Good white wine colors are white and green but we are flexible. Please don't use red, burgundy, or blue colors.

Target Market(s)

This wine label should appeal to all ages but be classy for the older crowd and still eye catching and fun for the millennials. This wine is sold in 15 states in the US, on the East Coast.

Industry/Entity Type

Town

Font styles to use
Serif
Sans Serif

Requirements
Must have
• Referring somehow or depicting the hill town and towers of San Gimignano in some way, such as in silhouette would be a plus. But also try to do something fun and unique with it-- not just an image of the town with words placed over it.
Should not have
• Please don't use the colors blue, reds. Try to think about what makes a wine label classy and sophisticated and 'upmarket' and what makes one cheap and cheesy. We are looking for the classy and sophisticated.

```html
<!DOCTYPE html>
<html lang="en">
<head>
<meta charset="utf-8">
<title>Cortivane – Vernaccia di San Gimignano Label</title>
<link href="https://fonts.googleapis.com/css2?family=Raleway:wght@300&family=Libre+Baskerville:wght@700&display=swap" rel="stylesheet">
<style>
  :root {
    --page: #ffffff;
    --label-black: #0b0b0b;
    --lattice-grey: #262626;
    --olive: #7b883b;
    --olive-text: #7a8a3a;
    --gold-dark: #a8692c;
    --gold-light: #f0d28a;
    --gold-mid: #c99250;
  }
  html, body {
    margin: 0;
    padding: 0;
    width: 1200px;
    height: 1000px;
    overflow: hidden;
    background: var(--page);
  }
  .canvas {
    position: relative;
    width: 1200px;
    height: 1000px;
  }
  .label {
    position: absolute;
    left: 148px;
    top: 216px;
    width: 525px;
    height: 579px;
    background: var(--label-black);
    overflow: hidden;
  }
  .label__lattice {
    position: absolute;
    inset: 0;
    background: radial-gradient(circle at 50% 50%, var(--lattice-grey) 0%, #141414 70%, var(--label-black) 100%);
  }
  .label__brand {
    position: absolute;
    left: 90px;
    top: 78px;
    width: 345px;
    margin: 0;
    font-family: "Raleway", "Helvetica Neue", Arial, sans-serif;
    font-weight: 300;
    font-size: 38px;
    line-height: 40px;
    letter-spacing: 0.34em;
    margin-right: -0.34em;
    color: var(--olive-text);
    text-align: justify;
    text-align-last: justify;
    text-transform: uppercase;
  }
  .label__rule {
    position: absolute;
    left: 89px;
    top: 136px;
    width: 346px;
    height: 6px;
    background: linear-gradient(90deg, var(--gold-dark) 0%, var(--gold-light) 45%, var(--gold-mid) 70%, var(--gold-dark) 100%);
  }
  .label__panel {
    position: absolute;
    left: 90px;
    top: 155px;
    width: 345px;
    height: 208px;
    background: var(--olive);
    display: flex;
    align-items: center;
    justify-content: center;
  }
  .label__panel-name {
    font-family: "Raleway", "Helvetica Neue", Arial, sans-serif;
    font-weight: 300;
    font-size: 30px;
    letter-spacing: 0.12em;
    color: var(--gold-light);
  }
  .label__varietal {
    position: absolute;
    left: 0;
    top: 394px;
    width: 100%;
    margin: 0;
    font-family: "Libre Baskerville", "Times New Roman", serif;
    font-weight: 700;
    font-size: 24px;
    line-height: 31px;
    color: var(--olive-text);
    text-align: center;
    text-transform: uppercase;
    letter-spacing: 0.01em;
  }
  .label__vintage {
    position: absolute;
    left: 0;
    top: 484px;
    width: 100%;
    margin: 0;
    font-family: "Raleway", "Helvetica Neue", Arial, sans-serif;
    font-weight: 300;
    font-size: 34px;
    color: var(--olive-text);
    text-align: center;
  }
</style>
</head>
<body>
<main class="canvas">
  <section class="label" aria-label="Front wine label">
    <div class="label__lattice" role="img" aria-label="Dark grey geometric lattice pattern covering the label background"></div>
    <h1 class="label__brand">Cortivane</h1>
    <div class="label__rule"></div>
    <div class="label__panel">
      <span class="label__panel-name">Cortivane</span>
    </div>
    <p class="label__varietal">Vernaccia<br>di San Gimignano</p>
    <p class="label__vintage">2016</p>
  </section>
</main>
</body>
</html>
```